Business Card

I need my new "Advisory" logo incorporated into my existing business card. I want the whole card redesigned. I would like to see a design with the existing colours and a few new colour options. The current card is not elegant or classy enough.

```html
<!DOCTYPE html>
<html lang="en">
<head>
<meta charset="utf-8">
<title>Novaterra Group – Business Card</title>
<link href="https://fonts.googleapis.com/css2?family=Arimo:wght@400;700&display=swap" rel="stylesheet">
<style>
  :root {
    --backdrop: #262626;
    --brand-blue: #2dbae0;
    --panel-black: #020202;
    --card-white: #f9f9fb;
    --text-white: #ffffff;
  }
  html, body {
    margin: 0;
    width: 1200px;
    height: 895px;
    overflow: hidden;
    background: var(--backdrop);
    font-family: "Arimo", Arial, sans-serif;
  }
  .card {
    position: absolute;
    left: 150px;
    top: 190px;
    width: 900px;
    height: 515px;
    display: flex;
    box-shadow: 0 12px 30px rgba(0,0,0,.45);
  }
  .card-front {
    width: 520px;
    height: 100%;
    background: var(--brand-blue);
    padding: 30px;
    box-sizing: border-box;
  }
  .info-panel {
    position: relative;
    width: 100%;
    height: 100%;
    background: var(--panel-black);
    border-radius: 20px;
    box-sizing: border-box;
    padding: 48px 40px 40px 44px;
    color: var(--text-white);
  }
  .company-name {
    margin: 0;
    font-weight: 700;
    font-size: 34px;
    line-height: 1.05;
    letter-spacing: .5px;
    color: var(--brand-blue);
  }
  .person {
    position: absolute;
    left: 150px;
    top: 230px;
  }
  .person-name {
    margin: 0;
    font-weight: 700;
    font-size: 30px;
    color: var(--brand-blue);
  }
  .person-title {
    margin: 2px 0 0;
    font-size: 19px;
    color: var(--text-white);
  }
  .contact-list {
    position: absolute;
    left: 150px;
    top: 335px;
    margin: 0;
    padding: 0;
    list-style: none;
    font-size: 17px;
  }
  .contact-item {
    display: flex;
    align-items: center;
    gap: 14px;
    height: 30px;
  }
  .contact-icon {
    width: 20px;
    height: 20px;
    flex: none;
  }
  .card-mark-side {
    flex: 1;
    background: var(--card-white);
    display: flex;
    align-items: center;
    justify-content: center;
    gap: 18px;
  }
  .mark-dot {
    width: 46px;
    height: 46px;
    border-radius: 50%;
    background: var(--brand-blue);
  }
  .mark-name {
    font-weight: 700;
    font-size: 40px;
    letter-spacing: 1px;
    color: var(--brand-blue);
  }
</style>
</head>
<body>
  <main class="card">
    <section class="card-front">
      <div class="info-panel">
        <h1 class="company-name">NOVATERRA<br>GROUP</h1>
        <div class="person">
          <h2 class="person-name">Marcus Ellory</h2>
          <p class="person-title">Managing Director</p>
        </div>
        <ul class="contact-list">
          <li class="contact-item">
            <svg class="contact-icon" viewBox="0 0 24 24" aria-hidden="true"><path fill="var(--brand-blue)" d="M6.6 10.8a15.1 15.1 0 0 0 6.6 6.6l2.2-2.2c.3-.3.7-.4 1-.2 1.1.4 2.3.6 3.6.6.6 0 1 .4 1 1V20c0 .6-.4 1-1 1A17 17 0 0 1 3 4c0-.6.4-1 1-1h3.5c.6 0 1 .4 1 1 0 1.3.2 2.5.6 3.6.1.3 0 .7-.2 1z"/></svg>
            <span>+61 400 123 987</span>
          </li>
          <li class="contact-item">
            <svg class="contact-icon" viewBox="0 0 24 24" aria-hidden="true"><g fill="none" stroke="var(--brand-blue)" stroke-width="1.6"><rect x="2" y="5" width="20" height="14"/><path d="M2 5l10 8 10-8M2 19l7-7M22 19l-7-7"/></g></svg>
            <span>marcus@novaterra.com.au</span>
          </li>
          <li class="contact-item">
            <svg class="contact-icon" viewBox="0 0 24 24" aria-hidden="true"><g fill="none" stroke="var(--brand-blue)" stroke-width="1.5"><circle cx="12" cy="12" r="9.5"/><ellipse cx="12" cy="12" rx="4.5" ry="9.5"/><path d="M2.5 12h19M4 7h16M4 17h16"/></g></svg>
            <span>https://novaterra.com.au</span>
          </li>
        </ul>
      </div>
    </section>
    <section class="card-mark-side">
      <span class="mark-dot"></span>
      <span class="mark-name">NOVATERRA</span>
    </section>
  </main>
</body>
</html>
```